依頼詳細
すでに手元にある名刺を見ていただけますか?

これを新たなデザインで刷新します。
必要なイラストや画像などはある程度ご用意できます。

何かこう見たときに「おぉ」となるようなデザインに変更できませんかね(´;ω;`)

奇抜なもの、スタイリッシュなもの、(この人はこんな感じなのだと)認識されやすいもののイメージです。

よろしくお願いします!
記載項目
森川塾:森川 晴人
電号:09058274316
メール:mrkw218@rakuhomail.jp

(裏面は特に希望無しです)
希望イメージ
シンプル 複雑
単色 カラフル
暗い 明るい
日常 高級
遊び心 厳粛
未来的 伝統的
女性的 男性的
希望する色
赤系、黄・オレンジ系、緑系、赤好み、虎は黄・黒、ネクタイは緑。ですが色に指定ありません。
納品ファイル
• PNG形式 (.png)
補足説明
ご不明な点がございましたらお気軽にメッセージください。
なにとぞよろしくお願いしますm(__)m
たくさんのご応募ありがとうございます!当選者が決まりました。

気に入った作品が多数あります。しかし予算上、満額は厳しいですが購入を考えています。

星マークの入った方にお声がけしていきますが、ご希望される方はその可否や条件をお知らせいただけるとスムーズです。

どうぞよろしくお願いします。
■ 選んだ理由

新しく描き起こしていただいた似顔絵はとても似ており、知り合いからも高評価です。
気に入ったので、修正依頼から即座に対応してもらえました。
誠にありがとうございます。

■ 提案者全員のお礼・コメント

ご提案いただきまして、誠にありがとうございました。
とても良いデザインがたくさん集まりました。
別途お声がけできればと考えています。

```html
<!DOCTYPE html>
<html lang="ja">
<head>
<meta charset="utf-8">
<title>森川塾 名刺</title>
<link href="https://fonts.googleapis.com/css2?family=Noto+Sans+JP:wght@400;500;700&display=swap" rel="stylesheet">
<style>
  :root {
    --stage: #8f8f8f;
    --label: #f2f2f2;
    --card: #ffffff;
    --board: #1f5a34;
    --board-frame: #b88a4e;
    --tray: #8a6233;
    --chalk: #ffffff;
    --ink: #222222;
    --portrait-skin: #e8c9a8;
    --portrait-hair: #3a2a20;
    --portrait-suit: #262d3a;
    --icon-light: #f4f7f5;
    --icon-mid: #b9d3c3;
    --maze-light: #f4f4f4;
    --maze-dark: #8a8a8a;
  }
  * { box-sizing: border-box; margin: 0; padding: 0; }
  html, body { width: 842px; height: 1200px; overflow: hidden; }
  body {
    background: var(--stage);
    font-family: "Noto Sans JP", sans-serif;
    position: relative;
  }
  .side-label {
    position: absolute; left: 0; width: 842px; text-align: center;
    color: var(--label); font-size: 22px; letter-spacing: 1px;
  }
  .side-label.front { top: 24px; }
  .side-label.back { top: 646px; }
  .card {
    position: absolute; left: 76px; width: 690px;
    background: var(--card);
    box-shadow: 6px 8px 14px rgba(0,0,0,.35);
  }
  .card.front { top: 84px; height: 480px; }
  .card.back { top: 700px; height: 418px; }

  .board {
    position: absolute; left: 16px; top: 16px; right: 16px; height: 420px;
    background: var(--board);
    border: 8px solid var(--board-frame);
    overflow: hidden;
  }
  .tray {
    position: absolute; left: 16px; right: 16px; top: 420px; height: 16px;
    background: var(--tray);
  }
  .portrait {
    position: absolute; left: 14px; top: 104px; width: 290px; height: 300px;
    background: linear-gradient(180deg, var(--portrait-hair) 0%, var(--portrait-hair) 14%, var(--portrait-skin) 24%, var(--portrait-skin) 62%, var(--portrait-suit) 80%, var(--portrait-suit) 100%);
    border-radius: 130px 130px 0 0;
  }
  .info { position: absolute; left: 345px; top: 60px; color: var(--chalk); }
  .role { font-size: 16px; line-height: 1.3; }
  .name { font-size: 36px; font-weight: 500; letter-spacing: 6px; line-height: 1.25; margin-top: 4px; }
  .romaji { font-size: 14px; letter-spacing: 2px; }
  .subjects { display: flex; align-items: flex-start; gap: 24px; margin-top: 30px; }
  .subjects-tag {
    writing-mode: vertical-rl; font-size: 14px; border: 2px solid var(--chalk);
    padding: 5px 3px; line-height: 1;
  }
  .subject { text-align: center; font-size: 14px; width: 62px; }
  .subject-icon {
    width: 54px; height: 54px; margin: 0 auto 6px;
    background: radial-gradient(circle at 50% 45%, var(--icon-light) 0%, var(--icon-mid) 60%, rgba(185,211,195,0) 72%);
  }
  .contact { margin-top: 30px; font-size: 15px; line-height: 1.55; }
  .contact-row { display: flex; align-items: center; gap: 8px; }
  .contact svg { width: 15px; height: 15px; flex: none; }

  .prompt {
    position: absolute; top: 52px; left: 0; width: 100%; text-align: center;
    font-size: 16px; color: var(--ink);
  }
  .maze-wrap { position: absolute; left: 244px; top: 100px; width: 204px; height: 240px; }
  .maze {
    position: absolute; left: 0; top: 16px; width: 204px; height: 212px;
    background: radial-gradient(ellipse at 50% 50%, var(--maze-light) 0%, #cfcfcf 55%, var(--maze-dark) 100%);
    border-radius: 40% 40% 44% 44%;
  }
  .maze-arrow { position: absolute; }
  .maze-arrow.in { left: 44px; top: -6px; }
  .maze-arrow.out { right: -26px; top: 200px; }
  .end-point { position: absolute; top: 218px; text-align: center; font-size: 13px; color: var(--ink); width: 120px; }
  .end-point.start { left: 58px; }
  .end-point.goal { left: 515px; }
  .end-icon {
    width: 60px; height: 38px; margin: 0 auto 10px;
    background: radial-gradient(ellipse at 50% 50%, #9a9a9a 0%, #d8d8d8 55%, rgba(255,255,255,0) 72%);
  }
</style>
</head>
<body>
  <div class="side-label front">omote</div>
  <section class="card front">
    <div class="board">
      <div class="portrait" role="img" aria-label="スーツに緑のネクタイでガッツポーズをする講師の似顔絵イラスト"></div>
    </div>
    <div class="tray"></div>
    <div class="info">
      <p class="role">家庭教師</p>
      <p class="name">森川 晴人</p>
      <p class="romaji">Haruto Morikawa</p>
      <div class="subjects">
        <span class="subjects-tag">授業科目</span>
        <div class="subject"><div class="subject-icon" role="img" aria-label="三角定規のイラスト"></div>数学</div>
        <div class="subject"><div class="subject-icon" role="img" aria-label="消しゴムと鉛筆のイラスト"></div>英語</div>
        <div class="subject"><div class="subject-icon" role="img" aria-label="フラスコのイラスト"></div>理科</div>
      </div>
      <div class="contact">
        <p>森川塾</p>
        <p class="contact-row">
          <svg viewBox="0 0 16 16"><path d="M4 1l3 3-2 2c1 2 3 4 5 5l2-2 3 3-2 3C7 15 1 9 1 3z" fill="#fff"/></svg>
          09058274316
        </p>
        <p class="contact-row">
          <svg viewBox="0 0 16 16"><rect x="1" y="3" width="14" height="10" fill="none" stroke="#fff" stroke-width="1.5"/><path d="M1 3l7 6 7-6" fill="none" stroke="#fff" stroke-width="1.5"/></svg>
          mrkw218@rakuhomail.jp
        </p>
      </div>
    </div>
  </section>

  <div class="side-label back">ura</div>
  <section class="card back">
    <p class="prompt">ボクの名前がかくれているよ! 名前を通ってゴールに行けるかな?</p>
    <div class="end-point start">
      <div class="end-icon" role="img" aria-label="ロードバイクのイラスト"></div>
      ロードバイク
    </div>
    <div class="maze-wrap">
      <svg class="maze-arrow in" width="14" height="20" viewBox="0 0 14 20"><path d="M7 0v16M2 11l5 6 5-6" fill="none" stroke="#222" stroke-width="2"/></svg>
      <div class="maze" role="img" aria-label="名前の文字が隠れた虎の顔の形の迷路"></div>
      <svg class="maze-arrow out" width="22" height="14" viewBox="0 0 22 14"><path d="M0 7h18M13 2l6 5-6 5" fill="none" stroke="#222" stroke-width="2"/></svg>
    </div>
    <div class="end-point goal">
      <div class="end-icon" role="img" aria-label="肝臓のイラスト"></div>
      肝臓
    </div>
  </section>
</body>
</html>
```